Harborne Cellarbook: the premier wine registry - (need business cards)

We have a logo designed, and now we need business cards for our 3 founders. Harborne Cellarbook is the premier wine registry for weddings. I am envisioning the wine glass with the heart in it as our signature symbol. (FYI- on the red background file, only use the part that has the red background; the brown colors are not relevant)

```html
<!DOCTYPE html>
<html lang="en">
<head>
<meta charset="utf-8">
<title>Harborne Cellarbook — Business Cards</title>
<link href="https://fonts.googleapis.com/css2?family=Montserrat:wght@400;500&family=Roboto:wght@400&display=swap" rel="stylesheet">
<style>
  :root {
    --backdrop: #bcbab8;
    --card: #ffffff;
    --wine: #94234a;
    --ink: #4a4a4a;
    --mist: #d3d3d3;
    --rule: #b5b5b5;
  }
  html, body {
    margin: 0;
    padding: 0;
    width: 1200px;
    height: 735px;
    overflow: hidden;
    background: var(--backdrop);
    font-family: "Montserrat", sans-serif;
  }
  .sheet { position: relative; width: 1200px; height: 735px; }
  .card {
    position: absolute;
    width: 550px;
    height: 318px;
    background: var(--card);
    box-shadow: -3px 3px 5px rgba(0,0,0,0.35);
  }
  .card--coo  { left: 33px;  top: 40px; }
  .card--ceo  { left: 613px; top: 40px; }
  .card--cfo  { left: 33px;  top: 386px; }
  .card--back { left: 613px; top: 386px; background: var(--wine); }

  .brand-name {
    position: absolute;
    left: 40px;
    top: 156px;
    width: 228px;
    text-align: center;
    font-weight: 500;
    font-size: 12px;
    letter-spacing: 2.6px;
    color: var(--wine);
    white-space: nowrap;
  }
  .divider {
    position: absolute;
    left: 274px;
    top: 110px;
    width: 1px;
    height: 102px;
    background: linear-gradient(to bottom, rgba(181,181,181,0), var(--rule) 20%, var(--rule) 80%, rgba(181,181,181,0));
  }
  .person { position: absolute; left: 290px; top: 103px; }
  .person__name {
    margin: 0;
    font-weight: 500;
    font-size: 20px;
    line-height: 22px;
    color: var(--wine);
  }
  .person__role {
    margin: 0;
    font-size: 12.5px;
    line-height: 16px;
    letter-spacing: 0.3px;
    color: var(--ink);
  }
  .contact {
    list-style: none;
    margin: 16px 0 0 1px;
    padding: 0;
    font-size: 12px;
    line-height: 16.5px;
    color: var(--ink);
  }
  .back-mark {
    position: absolute;
    left: 0; right: 0;
    top: 70px;
    text-align: center;
  }
  .back-mark__dot {
    display: block;
    margin: 0 auto 22px;
    width: 70px; height: 70px;
    border-radius: 50%;
    background: var(--mist);
  }
  .back-mark__name {
    font-weight: 500;
    font-size: 17px;
    letter-spacing: 4px;
    color: var(--mist);
  }
  .back-url {
    position: absolute;
    left: 0; right: 0;
    top: 256px;
    text-align: center;
    font-family: "Roboto", sans-serif;
    font-size: 12px;
    letter-spacing: 5px;
    color: #ffffff;
  }
</style>
</head>
<body>
<main class="sheet">
  <section class="card card--coo">
    <div class="brand-name">HARBORNE CELLARBOOK</div>
    <div class="divider"></div>
    <div class="person">
      <h2 class="person__name">MARCUS HALE</h2>
      <p class="person__role">CHIEF OPERATING OFFICER</p>
      <ul class="contact">
        <li>555-214-0381</li>
        <li>marcus@harbornecellarbook.com</li>
        <li>WWW.HARBORNECELLARBOOK.COM</li>
      </ul>
    </div>
  </section>

  <section class="card card--ceo">
    <div class="brand-name">HARBORNE CELLARBOOK</div>
    <div class="divider"></div>
    <div class="person">
      <h2 class="person__name">ELLIOT CRANE</h2>
      <p class="person__role">CHIEF EXECUTIVE OFFICER</p>
      <ul class="contact">
        <li>555-307-6629</li>
        <li>elliot@harbornecellarbook.com</li>
        <li>WWW.HARBORNECELLARBOOK.COM</li>
      </ul>
    </div>
  </section>

  <section class="card card--cfo">
    <div class="brand-name">HARBORNE CELLARBOOK</div>
    <div class="divider"></div>
    <div class="person">
      <h2 class="person__name">SIMON WARD</h2>
      <p class="person__role">CHIEF FINANCIAL OFFICER</p>
      <ul class="contact">
        <li>555-418-2750</li>
        <li>simon@harbornecellarbook.com</li>
        <li>WWW.HARBORNECELLARBOOK.COM</li>
      </ul>
    </div>
  </section>

  <section class="card card--back">
    <div class="back-mark">
      <span class="back-mark__dot"></span>
      <span class="back-mark__name">HARBORNE CELLARBOOK</span>
    </div>
    <div class="back-url">www.harbornecellarbook.com</div>
  </section>
</main>
</body>
</html>
```